Redesign wellness clinic website

The project is redesign a wellness clinic http://www.thornleighvitality.example. The new website is to be responsive,clean,bright and a strong call to action which is to book an appointment. The logo will remain the same but the colour scheme on the website should be reflect purple white and green. I want it to be bright and cheerful and the feeling of clarity. The website shouldn't be overloaded with content but more visuals.

Target Market(s)

Anyone that has corporate wellness benefits within the downtown Toronto core. Majority of audience are professional working in Media, Telecommunications and Investments.

Industry/Entity Type

Health And Wellness

Number of Pages Required

5+ page

Font styles to use
Sans Serif

Colors
ffffff
886aae
acd036

Requirements
Must have
• -Strong call to action which is book an appointment like this page https://www.kestrelmotion.example/
• -Services provided icons on the page like https://www.brightpathvitalityhouse.example/
• - Pictures of a good visualizing a fit and healthy life
• - Strong ratings from Quorva, Zintrel, PostMaz, similar to this website http://www.summitbalancehealth.example/our-team-professionals/
• - Bright and clear
Should not have
• -No black and white images (redo our pictures)
• -Dark themes

```html
<!DOCTYPE html>
<html lang="en">
<head>
<meta charset="utf-8">
<title>Thornleigh Vitality Centre</title>
<link href="https://fonts.googleapis.com/css2?family=Montserrat:wght@300;400;500;600&family=Open+Sans:wght@400;600&display=swap" rel="stylesheet">
<style>
:root{
  --purple:#886aae;
  --purple-dark:#7a5ea0;
  --green:#acd036;
  --white:#ffffff;
  --ink:#333333;
  --muted:#666666;
  --soft:#f4f4f6;
  --footer:#333333;
  --footer-deep:#2a2a2a;
  --footer-box:#3d3d3d;
  --rating-grey:#e6e6e6;
}
*{margin:0;padding:0;box-sizing:border-box}
html,body{width:1200px;height:2296px;overflow:hidden;background:var(--white)}
body{position:relative;font-family:"Open Sans",Arial,sans-serif;color:var(--ink)}
.abs{position:absolute}

/* Hero */
.hero{left:0;top:0;width:1200px;height:617px}
.hero-photo{left:0;top:0;width:1200px;height:617px;background:linear-gradient(100deg,#fbf9f7 0%,#f6f0ea 40%,#eedfd4 65%,#e9dcd2 100%)}
.menu-toggle{left:150px;top:50px;width:32px;height:20px}
.menu-toggle span{display:block;height:3px;background:var(--ink);margin-bottom:5px}
.brand{left:492px;top:38px;display:flex;align-items:center;gap:10px}
.brand-mark{width:44px;height:44px;border-radius:50%;background:var(--purple)}
.brand-name{font-family:"Montserrat",sans-serif;font-weight:600;font-size:13px;color:var(--purple);line-height:1.25}
.brand-name small{display:block;font-size:10px;font-weight:600;color:var(--purple)}
.hero-title{left:150px;top:212px;font-family:"Montserrat",sans-serif;font-weight:300;font-size:34px;line-height:44px;color:var(--ink);letter-spacing:.5px}
.hero-rule{left:392px;top:231px;width:262px;height:1px;background:var(--ink)}
.hero-lead{left:150px;top:318px;font-size:15px;color:var(--ink)}
.btn-book{left:150px;top:380px;width:210px;height:46px;background:var(--green);color:var(--white);font-family:"Montserrat",sans-serif;font-weight:500;font-size:12.5px;display:flex;align-items:center;justify-content:center;letter-spacing:.3px}

/* Services */
.services{left:0;top:617px;width:1200px;height:381px;background:var(--purple)}
.services-title{left:0;top:45px;width:1200px;text-align:center;color:var(--white);font-family:"Montserrat",sans-serif;font-weight:500;font-size:17px;letter-spacing:.5px}
.service-label{color:var(--white);font-family:"Montserrat",sans-serif;font-size:12.5px;width:240px;text-align:center;transform:translateX(-120px)}

/* Intro */
.intro-kicker{left:0;top:1064px;width:1200px;text-align:center;font-size:12px;color:var(--purple)}
.intro-title{left:0;top:1088px;width:1200px;text-align:center;font-family:"Montserrat",sans-serif;font-weight:400;font-size:25px;color:var(--ink)}
.intro-rule{left:585px;top:1126px;width:30px;height:2px;background:#e0e0e0}
.intro-text{left:168px;top:1141px;width:865px;text-align:center;font-size:11.6px;line-height:19.5px;color:var(--muted)}

/* Testimonial */
.testimonials{left:0;top:1296px;width:1200px;height:342px;background:linear-gradient(90deg,var(--green) 0%,#a6c63a 22%,#9a8f7a 45%,var(--purple) 62%,var(--purple) 100%)}
.testimonial-frame{left:152px;top:40px;width:893px;height:260px;border:2px solid var(--white)}
.testimonial-title{left:0;top:22px;width:889px;text-align:center;color:var(--white);font-family:"Montserrat",sans-serif;font-weight:300;font-size:26px}
.testimonial-name{left:0;top:62px;width:889px;text-align:center;color:var(--white);font-family:"Montserrat",sans-serif;font-size:15px;letter-spacing:.5px}
.testimonial-rule{left:264px;top:100px;width:406px;height:5px;border-top:1px solid var(--white);border-bottom:1px solid var(--white)}
.avatar{left:415px;top:128px;width:64px;height:56px;border:2px solid #c4302b;border-radius:4px;background:linear-gradient(135deg,#d7d7d7,#9a9a9a)}
.testimonial-quote{left:0;top:204px;width:889px;text-align:center;color:var(--white);font-size:12.5px}

/* Cards */
.card{background:var(--soft)}
.subscribe{left:144px;top:1697px;width:292px;height:380px}
.subscribe-head{left:6px;top:6px;width:280px;height:103px;background:var(--purple);color:var(--white);font-family:"Montserrat",sans-serif;font-weight:300;font-size:20px;line-height:31px;padding:20px 0 0 17px}
.subscribe-body{left:6px;top:109px;width:280px;height:265px;background:var(--white)}
.field{left:18px;width:244px;height:46px;border:1px solid #e4e4e4;border-radius:3px;font-size:10.5px;color:#888;padding:15px 0 0 14px}
.btn-subscribe{left:18px;top:142px;width:106px;height:44px;background:var(--green);color:var(--white);font-family:"Montserrat",sans-serif;font-weight:500;font-size:12px;display:flex;align-items:center;justify-content:center}

.blog{left:461px;top:1697px;width:290px;height:380px}
.blog-title{left:24px;top:24px;font-family:"Montserrat",sans-serif;font-size:21px;color:var(--ink)}
.post{left:24px;width:244px}
.post h3{font-family:"Montserrat",sans-serif;font-weight:400;font-size:13.5px;color:var(--ink);margin-bottom:7px}
.post time{display:block;font-size:10px;font-weight:600;color:var(--ink);margin-bottom:6px}
.post p{font-size:10px;line-height:15px;color:#888}
.post a{display:inline-block;margin-top:4px;font-size:10px;color:var(--purple);text-decoration:underline}
.post-divider{left:24px;width:244px;border-top:1px dashed #aaa}
.more-posts{right:22px;top:346px;font-size:10px;font-weight:600;color:var(--ink);text-decoration:underline;letter-spacing:.3px}

.ratings{left:776px;top:1697px;width:280px;height:380px}
.rating-logo{left:6px;width:268px;height:87px;background:var(--white);display:flex;align-items:center;justify-content:center;gap:10px;font-family:"Montserrat",sans-serif;font-weight:600;font-size:32px;color:var(--ink)}
.rating-logo i{display:block;width:22px;height:22px;background:var(--ink)}
.rating-bar{left:6px;width:268px;height:28px;display:flex;align-items:center;justify-content:space-between;padding:0 14px 0 16px;font-size:12px;color:var(--ink)}
.rating-bar.light{color:var(--white)}
.stars{letter-spacing:1px;font-size:14px}

/* Footer */
.footer{left:0;top:2132px;width:1200px;height:164px;background:var(--footer)}
.footer-brand{left:150px;top:0;width:245px;height:133px;background:var(--footer-box);display:flex;align-items:center;justify-content:center;gap:10px}
.footer-brand .brand-mark{width:44px;height:44px}
.footer-brand .brand-name{color:var(--white)}
.footer-brand .brand-name small{color:var(--white)}
.contact-title{left:464px;top:24px;color:var(--white);font-family:"Montserrat",sans-serif;font-size:15px}
.contact-item{color:#bdbdbd;font-size:11px;line-height:16px;display:flex;gap:8px;align-items:flex-start}
.legal{left:0;top:133px;width:1200px;height:31px;background:var(--footer-deep);font-size:10.5px;color:#9a9a9a}
.legal-copy{left:150px;top:9px}
.legal-links{left:456px;top:9px}
.social{top:5px;width:22px;height:22px}
</style>
</head>
<body>

<header class="hero abs">
  <div class="hero-photo abs" role="img" aria-label="Bright spa photo of a woman relaxing face-down on a massage table with white towels"></div>
  <div class="menu-toggle abs" aria-label="Menu"><span></span><span></span><span></span></div>
  <div class="brand abs">
    <div class="brand-mark"></div>
    <div class="brand-name">Thornleigh Vitality Centre<small>Call 555-204-7731</small></div>
  </div>
  <h1 class="hero-title abs">WELCOME TO<br>THORNLEIGH VITALITY CENTRE</h1>
  <div class="hero-rule abs"></div>
  <p class="hero-lead abs">Thornleigh Vitality Centre is a physiotherapist-owned clinic that has built...</p>
  <a class="btn-book abs">BOOK AN APPOINTMENT</a>
</header>

<section class="services abs">
  <h2 class="services-title abs">THORNLEIGH VITALITY SERVICES</h2>
  <svg class="abs" style="left:0;top:0" width="1200" height="381" viewBox="0 617 1200 381">
    <g stroke="#ffffff" stroke-width="1.2" fill="none" opacity=".8">
      <polyline points="190,876 328,778 464,876 608,778 735,876 872,778 1009,876"/>
    </g>
    <g fill="var(--purple)" stroke="#ffffff" stroke-width="2">
      <circle cx="328" cy="778" r="38"/><circle cx="608" cy="778" r="38"/><circle cx="872" cy="778" r="38"/>
      <circle cx="190" cy="876" r="38"/><circle cx="464" cy="876" r="38"/><circle cx="735" cy="876" r="38"/><circle cx="1009" cy="876" r="38"/>
    </g>
    <g fill="#ffffff">
      <circle cx="328" cy="778" r="31"/><circle cx="608" cy="778" r="31"/><circle cx="872" cy="778" r="31"/>
      <circle cx="190" cy="876" r="31"/><circle cx="464" cy="876" r="31"/><circle cx="735" cy="876" r="31"/><circle cx="1009" cy="876" r="31"/>
    </g>
    <g fill="var(--purple)">
      <!-- physiotherapy -->
      <circle cx="330" cy="766" r="4.5"/><rect x="314" y="780" width="30" height="5" rx="2"/><rect x="318" y="785" width="3" height="9"/><rect x="337" y="785" width="3" height="9"/><rect x="322" y="772" width="14" height="6" rx="3"/>
      <!-- massage -->
      <circle cx="612" cy="765" r="4.5"/><rect x="592" y="783" width="32" height="5" rx="2"/><rect x="598" y="776" width="20" height="6" rx="3"/><rect x="608" y="770" width="8" height="10" rx="3"/>
      <!-- osteopathy -->
      <rect x="869" y="758" width="6" height="40" rx="2"/><rect x="862" y="764" width="20" height="3" rx="1.5"/><rect x="862" y="772" width="20" height="3" rx="1.5"/><rect x="862" y="780" width="20" height="3" rx="1.5"/><ellipse cx="872" cy="795" rx="12" ry="5"/>
      <!-- chiropractic -->
      <circle cx="178" cy="870" r="4.5"/><rect x="172" y="877" width="34" height="5" rx="2"/><rect x="184" y="868" width="16" height="6" rx="3"/><rect x="176" y="882" width="3" height="8"/><rect x="199" y="882" width="3" height="8"/>
      <!-- rehab -->
      <circle cx="464" cy="860" r="5"/><rect x="456" y="868" width="16" height="18" rx="4"/><rect x="458" y="886" width="4" height="12"/><rect x="466" y="886" width="4" height="12"/>
      <!-- nutrition -->
      <path d="M735 866c-4-4-13-3-13 8 0 9 7 16 13 13 6 3 13-4 13-13 0-11-9-12-13-8z"/>
      <rect x="734" y="858" width="2.5" height="8" rx="1"/>
      <!-- chiropody -->
      <ellipse cx="1001" cy="882" rx="5" ry="9"/><ellipse cx="1017" cy="882" rx="5" ry="9"/>
      <circle cx="998" cy="868" r="2"/><circle cx="1003" cy="867" r="2"/><circle cx="1014" cy="867" r="2"/><circle cx="1019" cy="868" r="2"/>
    </g>
  </svg>
  <span class="service-label abs" style="left:328px;top:96px">Physiotherapy</span>
  <span class="service-label abs" style="left:608px;top:96px">Massage Therapy</span>
  <span class="service-label abs" style="left:872px;top:96px">Osteopathy</span>
  <span class="service-label abs" style="left:192px;top:313px">Chiropractic</span>
  <span class="service-label abs" style="left:464px;top:313px">Active Rehabilitation</span>
  <span class="service-label abs" style="left:735px;top:313px">Nutrition and Lifestyle Medicine</span>
  <span class="service-label abs" style="left:1007px;top:313px">Chiropody</span>
</section>

<section class="intro">
  <p class="intro-kicker abs">Come and join our Family and start changing your life today.</p>
  <h2 class="intro-title abs">Welcome to Thornleigh Vitality Center</h2>
  <div class="intro-rule abs"></div>
  <p class="intro-text abs">Established in 1989 the Thornleigh Vitality Centre has become one of Canada's leaders in providing quality care and innovative wellness programs for the community. The founder and director Dr. Elias Varnum's vision has come to life with over 30 practitioners providing a multitude of different services under one roof. Some of the services include Chiropractic, Physiotherapy, Athletic Therapy, Naturopathy, Massage Therapy, Acupuncture and Personal Training. The Thornleigh Vitality Centre has a complete Pilates studio on its premises. We also offer many wellness seminars free of cost to the public.&nbsp;&nbsp; Our Centre is committed to helping improve and extend the lives of as many people as possible in our community.</p>
</section>

<section class="testimonials abs">
  <div class="testimonial-frame abs">
    <h2 class="testimonial-title abs">What Our Customer Says</h2>
    <p class="testimonial-name abs">JENNA ASHCROFT</p>
    <div class="testimonial-rule abs"></div>
    <div class="avatar abs" role="img" aria-label="Customer portrait thumbnail"></div>
    <p class="testimonial-quote abs">Dear Dr. Halvik: I attended your clinic recently and was surprised. I am 68 years old and never before was...</p>
  </div>
</section>

<section class="card subscribe abs">
  <h2 class="subscribe-head abs">Subscribe To<br>Our Mailing List</h2>
  <form class="subscribe-body abs">
    <div class="field abs" style="top:28px">Name</div>
    <div class="field abs" style="top:78px">Enter Your Email</div>
    <a class="btn-subscribe abs">SUBSCRIBE</a>
  </form>
</section>

<section class="card blog abs">
  <h2 class="blog-title abs">Our Blog</h2>
  <article class="post abs" style="top:66px">
    <h3>Think Well Program</h3>
    <time>Monday, June 5, 2017 - 09:29</time>
    <p>Did you know that your mental wellness can directly affect your physical wellness, and vice versa? Our Think Well program comprises...</p>
    <a>Read More</a>
  </article>
  <div class="post-divider abs" style="top:186px"></div>
  <article class="post abs" style="top:206px">
    <h3>Think Well Program</h3>
    <time>Monday, June 5, 2017 - 09:29</time>
    <p>Did you know that your mental wellness can directly affect your physical wellness, and vice versa? Our Think Well program comprises...</p>
    <a>Read More</a>
  </article>
  <div class="post-divider abs" style="top:326px"></div>
  <a class="more-posts abs">MORE POSTS</a>
</section>

<section class="card ratings abs">
  <div class="rating-logo abs" style="top:6px"><i></i>Quorva</div>
  <div class="rating-bar abs" style="top:93px;background:var(--rating-grey)"><span>Quorva Rating</span><span class="stars">★★★★☆</span></div>
  <div class="rating-logo abs" style="top:132px"><i></i>Zintrel</div>
  <div class="rating-bar light abs" style="top:219px;background:var(--purple)"><span>Zintrel Rating</span><span class="stars">★★★★☆</span></div>
  <div class="rating-logo abs" style="top:258px"><i></i>PostMaz</div>
  <div class="rating-bar light abs" style="top:345px;background:var(--green)"><span>PostMaz Rating</span><span class="stars">★★★★☆</span></div>
</section>

<footer class="footer abs">
  <div class="footer-brand abs">
    <div class="brand-mark"></div>
    <div class="brand-name">Thornleigh Vitality Centre<small>Call 555-204-7731</small></div>
  </div>
  <h2 class="contact-title abs">Contact us</h2>
  <div class="contact-item abs" style="left:464px;top:52px">
    <svg width="10" height="14" viewBox="0 0 10 14"><path d="M5 0a5 5 0 0 0-5 5c0 4 5 9 5 9s5-5 5-9a5 5 0 0 0-5-5zm0 7a2 2 0 1 1 0-4 2 2 0 0 1 0 4z" fill="#9a9a9a"/></svg>
    <span>Thornleigh Vitality Centre<br>48 Larkmoor Avenue East, Suite 210</span>
  </div>
  <div class="contact-item abs" style="left:686px;top:54px">
    <svg width="9" height="14" viewBox="0 0 9 14"><rect x=".5" y=".5" width="8" height="13" rx="1.5" fill="none" stroke="#9a9a9a"/><rect x="3" y="11" width="3" height="1" fill="#9a9a9a"/></svg>
    <span>555-204-7731</span>
  </div>
  <div class="contact-item abs" style="left:842px;top:54px">
    <svg width="14" height="10" viewBox="0 0 14 10"><rect x=".5" y=".5" width="13" height="9" fill="none" stroke="#9a9a9a"/><path d="M.5.5 7 6l6.5-5.5" fill="none" stroke="#9a9a9a"/></svg>
    <span>appointments@thornleighvitality.example</span>
  </div>
  <div class="legal abs">
    <span class="legal-copy abs">©2017 Thornleigh Vitality Center, Allrights are Reserved.</span>
    <span class="legal-links abs">Privacy Policy | Returns &amp; Refunds | Terms &amp; Conditions | Login</span>
    <span class="social abs" style="left:988px;background:#3b5998"></span>
    <span class="social abs" style="left:1020px;background:#1da1f2"></span>
  </div>
</footer>

</body>
</html>
```